Plate Bright Workshop (workshop to teach people to eat fruits and vegetables)

Double sided DL Flyer

Free Community Workshop
Plate Bright Live Lively
Central Coast NSW

Copy to appear on flyer side one:-
PLATE BRIGHT LIVE LIVELY
interactive workshops
March-April 2019
Presented by qualified nutritionist

Food for healthier happier life for you and your family (free to central coast residents - all ages welcome

Side 2
Learn About:-
Foods that improve your health
basic nutrition
gut brain connection
portion size
menu planning
preparation
eating

Benefits
Improved health
Improved Energy
Manage chronic illness
diabetes type II
cholesterol
Blood Pressure
Family fun

Food Tastings
Lucky Door Prize

Reserve for spot online @ www.platebright.com.au or call 0462 508 731
Supported by Harbourline Shire Council (Logo) Harbourline Rugby Social Club (Logo) Pindara Veterans Club (Logo)

I would like to see a flyer that is bright, fun and fresh with images of fresh food.

Target Market(s)

Women 30 plus

Industry/Entity Type

Health And Wellness

Logo Text

PLATE BRIGHT LIVE LIVELY

Font styles to use
Other font styles liked:
• bold clean

Colors
f37122
9bcb3c
fbed22
ec1f27
e34297

Requirements
Must have
• bright eye catching colours featuring fresh fruit and vegetables
• I have attached a some images of designs I like
Nice to have
• Im happy for the designer to change copy to create a clean flyer without loosing essential information
• I like the feel of the banner on my facebook page
• Kindly Nourish - Plate Bright Live Lively with Megan Troute
• https://www.facebook.com/kindlynourishoz/
Should not have
• old fashioned images

```html
<!DOCTYPE html>
<html lang="en">
<head>
<meta charset="utf-8">
<title>Plate Bright Live Lively – DL Flyer</title>
<link rel="stylesheet" href="https://fonts.googleapis.com/css2?family=Montserrat:wght@500;700;800;900&family=Open+Sans:wght@400;600;700&display=swap">
<style>
  :root{
    --stage:#cbcbcb;
    --pink:#e6197f;
    --green:#9bcb3c;
    --green-dark:#7fb52a;
    --yellow:#fbed22;
    --orange:#f37122;
    --ink:#1d1d1b;
    --white:#ffffff;
    --head:'Montserrat', sans-serif;
    --body:'Open Sans', sans-serif;
  }
  *{box-sizing:border-box;margin:0;padding:0}
  html,body{width:1200px;height:858px;overflow:hidden;background:var(--stage)}
  .stage{position:relative;width:1200px;height:858px}
  .flyer{position:absolute;top:34px;width:370px;height:790px;background:var(--white);overflow:hidden;box-shadow:0 6px 18px rgba(0,0,0,.18)}
  .flyer--front{left:200px}
  .flyer--back{left:630px}
  .layer{position:absolute;left:0;top:0}
  .abs{position:absolute}
  .icon{width:12px;height:12px;flex:none}
  .contact-row{font-family:var(--body);font-size:10.5px;line-height:1.45;color:var(--white);display:flex;align-items:center;gap:6px}
  .contact-row b{font-family:var(--head);font-weight:700}

  /* SIDE ONE */
  .front-photo{position:absolute;left:0;top:0;width:370px;height:260px;background:linear-gradient(135deg,#b88a5e 0%,#e2462b 35%,#f08a2a 55%,#6aa83a 80%,#d9c7a8 100%)}
  .brand{left:24px;top:280px;display:flex;align-items:center;gap:10px}
  .brand__dot{width:32px;height:32px;border:3px solid var(--pink);border-radius:50%}
  .brand__name{font-family:var(--head);font-weight:500;font-size:21px;letter-spacing:1px;color:var(--ink);text-transform:uppercase}
  .title-band{left:0;top:326px;width:370px;height:46px;background:var(--green);display:flex;align-items:center;padding-left:20px}
  .title{font-family:var(--head);font-weight:900;font-size:23px;color:var(--ink);letter-spacing:-.3px}
  .title span{color:var(--pink)}
  .meta{left:20px;top:382px;font-family:var(--head);font-weight:700;font-size:12.5px;color:var(--ink);text-transform:uppercase}
  .meta .date{color:var(--pink);text-transform:none;margin-left:6px}
  .meta .presented{display:block;margin-top:4px;color:var(--green-dark)}
  .meta .presented b{color:var(--pink)}
  .headline{left:20px;top:430px;width:330px;font-family:var(--head);font-weight:900;font-size:17px;line-height:1.15;color:var(--ink);text-transform:uppercase}
  .intro{left:20px;top:478px;width:330px;font-family:var(--body);font-size:11.5px;line-height:1.4;color:var(--ink)}
  .free-band{left:0;top:598px;width:370px;height:60px;background:var(--green);padding:8px 20px}
  .free-band__small{font-family:var(--head);font-weight:800;font-size:13px;color:var(--ink);text-transform:uppercase}
  .free-band__big{font-family:var(--head);font-weight:900;font-size:24px;color:var(--pink);text-transform:uppercase;line-height:1.1}
  .contact{left:20px;top:696px}
  .contact__call{font-family:var(--head);font-weight:800;font-size:15px;color:var(--white);margin-bottom:2px}
  .contact__call .phone{color:var(--yellow);font-size:22px;margin-left:8px}

  /* SIDE TWO */
  .back-photo-woman{position:absolute;right:0;top:0;width:190px;height:130px;background:linear-gradient(160deg,#eaf2f5,#bcd6de 60%,#dbe9c8)}
  .back-bg-fruit{position:absolute;left:0;top:150px;width:370px;height:400px;background:radial-gradient(circle at 70% 30%,#f3f1d7 0,#f7e6d6 35%,#fbf3ea 70%,#ffffff 100%)}
  .back-photo-fruit{position:absolute;right:0;top:540px;width:220px;height:120px;background:radial-gradient(circle at 40% 50%,#d83a2a 0,#8fbf3a 45%,#4f8b2c 80%,#ffffff 100%)}
  .back-title{left:22px;top:40px;font-family:var(--head);font-weight:900;font-size:28px;line-height:1.05;text-transform:uppercase}
  .back-title .l1{color:var(--pink);display:block}
  .back-title .l2{color:var(--white);display:block}
  .list-block{left:28px;font-family:var(--head)}
  .list-block h3{font-weight:800;font-size:15px;color:var(--ink);margin-bottom:4px}
  .list-block ul{list-style:none}
  .list-block li{font-weight:700;font-size:13px;color:var(--pink);line-height:1.55;display:flex;align-items:center;gap:7px}
  .list-block li::before{content:"";width:7px;height:7px;border:1.5px solid var(--ink);border-radius:50%;flex:none}
  .learn{top:200px}
  .benefits{top:372px}
  .badge{left:232px;top:300px;width:118px;height:118px;border-radius:50%;background:var(--yellow);border:5px solid var(--pink);box-shadow:0 0 0 4px var(--green);display:flex;flex-direction:column;align-items:center;justify-content:center;text-align:center;font-family:var(--head);line-height:1}
  .badge .tastings{color:var(--pink);font-weight:800;font-size:14px}
  .badge .lucky{color:var(--white);font-weight:900;font-size:22px;margin-top:3px;background:var(--pink);padding:2px 6px}
  .badge .prize{color:var(--ink);font-weight:700;font-size:9px;margin-top:4px;text-transform:uppercase}
  .back-contact{left:22px;top:668px;width:330px}
  .back-contact .phone{font-family:var(--head);font-weight:800;font-size:20px;color:var(--white);display:flex;align-items:center;gap:8px;margin-bottom:1px}
  .supporters{margin-top:3px;font-family:var(--body);font-size:9px;color:var(--white);display:flex;flex-wrap:wrap;gap:3px 10px;align-items:center}
  .supporters__label{font-family:var(--head);font-weight:700;width:100%}
  .supporter{display:flex;align-items:center;gap:4px}
  .supporter::before{content:"";width:8px;height:8px;border-radius:50%;background:var(--white);flex:none}
</style>
</head>
<body>
<main class="stage">

  <section class="flyer flyer--front" aria-label="Flyer side one">
    <div class="front-photo" role="img" aria-label="Photo of a basket of fresh vegetables and fruit: tomatoes, carrots, lettuce, strawberries, watermelon and lemons"></div>
    <svg class="layer" width="370" height="790" viewBox="0 0 370 790" aria-hidden="true">
      <path d="M0 268 C120 268 250 225 370 150 L370 326 L0 326 Z" fill="#fff"/>
      <path d="M0 268 C120 268 250 225 370 150" fill="none" stroke="#e6197f" stroke-width="6"/>
      <path d="M0 259 C120 259 250 214 370 138" fill="none" stroke="#9bcb3c" stroke-width="7"/>
      <path d="M0 672 C110 680 250 664 370 640 L370 790 L0 790 Z" fill="#f37122"/>
      <path d="M0 680 C110 688 250 672 370 650 L370 790 L0 790 Z" fill="#9bcb3c"/>
      <path d="M0 688 C110 696 250 682 370 660 L370 790 L0 790 Z" fill="#e6197f"/>
    </svg>

    <div class="abs brand">
      <span class="brand__dot"></span>
      <span class="brand__name">Kindly Nourish</span>
    </div>

    <div class="abs title-band"><h1 class="title">PLATE BRIGHT <span>LIVE LIVELY</span></h1></div>

    <p class="abs meta">Interactive Workshops <span class="date">March-April 2019</span>
      <span class="presented">Presented by <b>Qualified Nutritionist</b></span></p>

    <h2 class="abs headline">Food for a healthier happier life for you and your family</h2>

    <p class="abs intro">Our most important asset is our health! So why is it that we spend money on material possessions before spending money on our most important possession? Investing in your health has a flow on effect to every other part of your life helping you to be successful in whatever your dreams may be! Love yourself with what you put in.</p>

    <div class="abs free-band">
      <p class="free-band__small">Free for NSW Central Coast residents</p>
      <p class="free-band__big">All ages welcome</p>
    </div>

    <div class="abs contact">
      <p class="contact__call">CALL NOW:<span class="phone">0462 508 731</span></p>
      <p class="contact-row"><b>Reserve online:</b> www.platebright.com.au</p>
      <p class="contact-row">
        <svg class="icon" viewBox="0 0 12 12"><rect x="1" y="2.5" width="10" height="7" rx="1" fill="none" stroke="#fff" stroke-width="1.2"/><path d="M1.5 3 6 6.5 10.5 3" fill="none" stroke="#fff" stroke-width="1.2"/></svg>
        megan@kindlynourish.com.au</p>
      <p class="contact-row"><b>Follow Us:</b> @kindlynourishoz</p>
      <p class="contact-row">
        <svg class="icon" viewBox="0 0 12 12"><path d="M6 11S2 7 2 4.5a4 4 0 0 1 8 0C10 7 6 11 6 11Z" fill="#fff"/><circle cx="6" cy="4.5" r="1.4" fill="#e6197f"/></svg>
        4/18 Marlowe Crescent, Seabrook NSW 2261</p>
    </div>
  </section>

  <section class="flyer flyer--back" aria-label="Flyer side two">
    <svg class="layer" width="370" height="790" viewBox="0 0 370 790" aria-hidden="true">
      <path d="M0 0 H370 V150 C250 140 120 170 0 240 Z" fill="#9bcb3c"/>
    </svg>
    <div class="back-photo-woman" role="img" aria-label="Photo of a smiling young woman holding a bowl of salad"></div>
    <div class="back-bg-fruit" role="img" aria-label="Faded background photo of apples, onions and fresh produce"></div>
    <svg class="layer" width="370" height="790" viewBox="0 0 370 790" aria-hidden="true">
      <path d="M0 0 H180 V130 C130 130 60 170 0 220 Z" fill="#9bcb3c"/>
      <path d="M0 236 C110 170 250 140 370 150" fill="none" stroke="#e6197f" stroke-width="5"/>
      <path d="M0 246 C110 180 250 152 370 160" fill="none" stroke="#fbed22" stroke-width="4"/>
    </svg>
    <div class="back-photo-fruit" role="img" aria-label="Photo of grapes, red apples, bananas and leafy greens"></div>
    <svg class="layer" width="370" height="790" viewBox="0 0 370 790" aria-hidden="true">
      <path d="M0 548 C50 600 100 636 150 656 L150 660 L0 660 Z" fill="#fff"/>
      <path d="M0 548 C50 600 100 636 160 658" fill="none" stroke="#e6197f" stroke-width="6"/>
      <path d="M0 562 C50 612 95 642 150 660" fill="none" stroke="#9bcb3c" stroke-width="5"/>
      <rect x="0" y="658" width="370" height="132" fill="#e6197f"/>
    </svg>

    <h2 class="abs back-title"><span class="l1">Plate Bright</span><span class="l2">Live Lively</span></h2>

    <div class="abs list-block learn">
      <h3>Learn About</h3>
      <ul>
        <li>Portion Size</li>
        <li>Basic Nutrition</li>
        <li>Foods that improve your health</li>
        <li>Gut Brain Connection</li>
        <li>Menu Planning</li>
        <li>Preparation</li>
        <li>Eating</li>
      </ul>
    </div>

    <div class="abs list-block benefits">
      <h3>Benefits</h3>
      <ul>
        <li>Improved Health</li>
        <li>Improved Energy</li>
        <li>Manage Chronic Illness</li>
        <li>Diabetes Type II</li>
        <li>Cholesterol</li>
        <li>Blood Pressure</li>
        <li>Family Fun</li>
      </ul>
    </div>

    <div class="abs badge">
      <span class="tastings">Food<br>Tastings</span>
      <span class="lucky">LUCKY</span>
      <span class="prize">Door Prize</span>
    </div>

    <div class="abs back-contact">
      <p class="phone">
        <svg class="icon" viewBox="0 0 12 12"><path d="M3 1 5 3.5 4 5c.6 1.3 1.7 2.4 3 3l1.5-1L11 9 9.5 11C5 11 1 7 1 2.5Z" fill="#fff"/></svg>
        0462-508-731</p>
      <p class="contact-row"><b>Reserve your spot:</b> www.platebright.com.au</p>
      <p class="contact-row"><b>Follow Us:</b> @kindlynourishoz</p>
      <p class="contact-row">
        <svg class="icon" viewBox="0 0 12 12"><path d="M6 11S2 7 2 4.5a4 4 0 0 1 8 0C10 7 6 11 6 11Z" fill="#fff"/><circle cx="6" cy="4.5" r="1.4" fill="#e6197f"/></svg>
        4/18 Marlowe Crescent, Seabrook NSW 2261</p>
      <div class="supporters">
        <span class="supporters__label">Supported by</span>
        <span class="supporter">Harbourline Shire Council</span>
        <span class="supporter">Harbourline Rugby Social Club</span>
        <span class="supporter">Pindara Veterans Club</span>
      </div>
    </div>
  </section>

</main>
</body>
</html>
```